Calder Pizza - Takeout Menu Design

We are looking for a takeout menu design.
We are looking for a( 5" x 8.5" DOUBLE SIDED) flyer with our available pizza flavors
Must be easy to ready and not "busy"

Must include our logo (attached)
website: www.calderpizza.ca
address:
Fenwick Ridge Plaza
417, 318 9 Avenue SW
and the following details:
Visit our website for our complete appetizer, pasta, salad and catering menu.

Winner of this contest will also be offered to create a few print designs via printhive.

Please do not hesitate to ask any questions.

Target Market(s)

Business / Office clientele

Industry/Entity Type

Pizza place / specializing in corporate orders

Requirements
Must have
• Easy to read
Should not have
• Can not be busy or cluttered

```html
<!DOCTYPE html>
<html lang="en">
<head>
<meta charset="utf-8">
<title>Calder Pizza – Takeout Menu</title>
<link href="https://fonts.googleapis.com/css2?family=Montserrat:ital,wght@0,300;0,400;0,500;0,600;1,400;1,600;1,700&display=swap" rel="stylesheet">
<style>
  :root {
    --brand-red: #c0302a;
    --ink: #1c1c1c;
    --muted: #9a9a9a;
    --rule: #c9c9c9;
    --paper: #ffffff;
    --stage: #ffffff;
    --crust: #d99a4e;
    --sauce: #c9452c;
  }
  * { box-sizing: border-box; margin: 0; padding: 0; }
  html, body { width: 1200px; height: 900px; overflow: hidden; background: var(--stage); }
  body { position: relative; font-family: "Montserrat", Arial, sans-serif; color: var(--ink); }

  .menu-page {
    position: absolute; top: 44px; width: 477px; height: 812px;
    background: var(--paper); overflow: hidden;
    box-shadow: 0 6px 14px rgba(0,0,0,0.18);
  }
  .menu-page--front { left: 104px; }
  .menu-page--back { left: 619px; }

  .band { position: absolute; left: 0; width: 100%; display: block; }
  .band--top { top: 0; height: 74px; }
  .band--bottom { bottom: 0; height: 86px; }

  .intro {
    position: absolute; left: 34px; top: 32px;
    color: #fff; font-size: 10.5px; line-height: 14px; font-weight: 400;
  }

  .pizza-photo { position: absolute; border-radius: 50%;
    background: radial-gradient(circle at 45% 45%, #e9b15a 0%, var(--sauce) 45%, #b43b22 62%, var(--crust) 72%, #b97a35 100%); }
  .pizza-photo--corner { width: 120px; height: 120px; right: -46px; top: -8px; }
  .pizza-photo--hero { width: 220px; height: 220px; right: -30px; bottom: -123px; }

  .section-title {
    position: absolute; left: 34px;
    color: var(--brand-red); font-size: 16px; font-weight: 700; font-style: italic;
  }
  .section-title--classic { top: 80px; }
  .section-title--specialty { top: 248px; }

  .price-list { position: absolute; left: 34px; right: 33px; list-style: none; }
  .price-list--classic { top: 106px; }
  .price-list--specialty { top: 279px; }
  .price-list--back { top: 33px; }

  .classic-row {
    display: flex; align-items: center; height: 16.4px;
    border-bottom: 1px solid var(--rule); font-size: 10.5px;
  }
  .classic-row:last-child { border-bottom: none; }
  .classic-row .name { flex: 1; }

  .prices { display: flex; font-size: 10.5px; font-weight: 700; font-style: italic; }
  .prices span { width: 46px; text-align: right; }

  .pizza-item {
    display: flex; padding: 3px 0 2px; border-bottom: 1px solid var(--rule);
  }
  .pizza-item:last-child { border-bottom: none; }
  .pizza-item .detail { flex: 1; }
  .pizza-item .name {
    font-size: 10.5px; font-weight: 600; font-style: italic; line-height: 14px; margin-bottom: 3px;
  }
  .pizza-item .desc { font-size: 10.5px; line-height: 13px; }
  .pizza-item .prices { line-height: 14px; }
  .prices--stacked { flex-direction: column; }
  .prices--stacked div { display: flex; line-height: 13px; }

  .tax-note {
    position: absolute; right: 34px; top: 716px;
    font-size: 10px; font-style: italic; color: var(--muted);
  }

  .brand { position: absolute; left: 34px; bottom: 20px; color: #fff; }
  .brand-name {
    font-size: 21px; font-weight: 400; letter-spacing: 0.5px; line-height: 24px; text-transform: uppercase;
  }
  .brand-url { font-size: 10.5px; line-height: 14px; font-weight: 400; }

  .address {
    position: absolute; right: 34px; bottom: 33px;
    color: #fff; font-size: 10.5px; line-height: 13px; text-align: right; font-style: normal;
  }
</style>
</head>
<body>

<section class="menu-page menu-page--front">
  <svg class="band band--top" viewBox="0 0 477 74" preserveAspectRatio="none" aria-hidden="true">
    <path fill="var(--brand-red)" d="M0 0H477V66L470 68L462 66L451 69L440 67L428 70L415 67L402 69L390 66L378 69L365 67L350 70L336 67L322 69L310 66L296 69L282 67L268 70L254 67L240 69L226 66L212 69L198 67L184 70L170 67L156 69L142 66L128 69L114 67L100 70L86 67L72 69L58 66L44 69L30 67L16 70L0 67Z"/>
  </svg>
  <p class="intro">All of our pizzas are prepared fresh everyday<br>using only the finest mozzarella blend and ingredients.</p>
  <div class="pizza-photo pizza-photo--corner" role="img" aria-label="Photo of a whole pizza with toppings"></div>

  <h2 class="section-title section-title--classic">Classic Take-Out Pizza - 8" &amp; 13"</h2>
  <ul class="price-list price-list--classic">
    <li class="classic-row"><span class="name">Pepperoni &amp; Mushroom</span><span class="prices"><span>$12.99</span><span>$30.95</span></span></li>
    <li class="classic-row"><span class="name">Pepperoni</span><span class="prices"><span>$11.99</span><span>$29.95</span></span></li>
    <li class="classic-row"><span class="name">Hawaiian</span><span class="prices"><span>$12.99</span><span>$30.95</span></span></li>
    <li class="classic-row"><span class="name">Beef &amp; Mushroom</span><span class="prices"><span>$13.49</span><span>$32.95</span></span></li>
    <li class="classic-row"><span class="name">Pepperoni &amp; Ham</span><span class="prices"><span>$12.99</span><span>$30.95</span></span></li>
    <li class="classic-row"><span class="name">Ham &amp; Mushroom</span><span class="prices"><span>$12.99</span><span>$30.95</span></span></li>
    <li class="classic-row"><span class="name">Beef &amp; Onion</span><span class="prices"><span>$13.49</span><span>$32.95</span></span></li>
    <li class="classic-row"><span class="name">Cheese</span><span class="prices"><span>$11.99</span><span>$29.95</span></span></li>
  </ul>

  <h2 class="section-title section-title--specialty">Specialty Take-Out Pizza- 8" &amp; 13"</h2>
  <ul class="price-list price-list--specialty">
    <li class="pizza-item"><div class="detail"><p class="name">All Meat</p><p class="desc">Pepperoni, Beef &amp; Smoked Ham &amp; Bacon</p></div><div class="prices"><span>$14.99</span><span>$35.95</span></div></li>
    <li class="pizza-item"><div class="detail"><p class="name">Double Pepperoni</p><p class="desc">Loads of Pepperoni</p></div><div class="prices"><span>$13.49</span><span>$32.95</span></div></li>
    <li class="pizza-item"><div class="detail"><p class="name">Hot Honey Pepperoni</p><p class="desc">Double Pepperoni and drizzled with Hot Honey</p></div><div class="prices"><span>$14.49</span><span>$34.95</span></div></li>
    <li class="pizza-item"><div class="detail"><p class="name">Hawaiian Heat</p><p class="desc">Smoked Ham, Pineapple and Banana Peppers</p></div><div class="prices"><span>$13.49</span><span>$32.95</span></div></li>
    <li class="pizza-item"><div class="detail"><p class="name">Four Cheese</p><p class="desc">Mozzarella, Feta, Romano and Cheddar Cheese</p></div><div class="prices"><span>$13.49</span><span>$32.95</span></div></li>
    <li class="pizza-item"><div class="detail"><p class="name">Montreal</p><p class="desc">Pepperoni &amp; Double Smoked Bacon</p></div><div class="prices"><span>$13.49</span><span>$32.95</span></div></li>
    <li class="pizza-item"><div class="detail"><p class="name">Montreal Heat</p><p class="desc">Pepperoni,&nbsp; Double Smoked Bacon<br>&amp; Banana Peppers</p></div><div class="prices"><span>$13.99</span><span>$33.95</span></div></li>
    <li class="pizza-item"><div class="detail"><p class="name">Supreme</p><p class="desc">Pepperoni, Mushrooms &amp; Green Peppers</p></div><div class="prices"><span>$13.49</span><span>$32.95</span></div></li>
    <li class="pizza-item"><div class="detail"><p class="name">Canadian</p><p class="desc">Pepperoni, Mushrooms &amp; Ham</p></div><div class="prices"><span>$13.49</span><span>$32.95</span></div></li>
    <li class="pizza-item"><div class="detail"><p class="name">BBQ Chicken</p><p class="desc">Chicken Breast, Hickory BBQ Sauce &amp; Red Onions</p></div><div class="prices"><span>$13.99</span><span>$33.95</span></div></li>
    <li class="pizza-item"><div class="detail"><p class="name">BBQ Chicken Plus</p><p class="desc">Chicken Breast, Hickory BBQ Sauce,<br>Red Onions &amp; Cilantro</p></div><div class="prices"><span>$14.79</span><span>$34.95</span></div></li>
  </ul>

  <p class="tax-note">GST not included</p>

  <svg class="band band--bottom" viewBox="0 0 477 86" preserveAspectRatio="none" aria-hidden="true">
    <path fill="var(--brand-red)" d="M0 6L14 3L28 6L42 2L56 5L70 3L84 6L98 2L112 5L126 3L140 6L154 2L168 5L182 3L196 6L210 2L224 5L238 3L252 6L266 2L280 5L294 3L308 6L322 2L336 5L350 3L364 6L378 2L392 5L406 3L420 6L434 2L448 5L462 3L477 5V86H0Z"/>
  </svg>
  <div class="brand">
    <p class="brand-name">Calder Pizza</p>
    <p class="brand-url">calderpizza.ca</p>
  </div>
  <address class="address">Fenwick Ridge Plaza<br>417, 318 9 Avenue SW</address>
</section>

<section class="menu-page menu-page--back">
  <ul class="price-list price-list--back">
    <li class="pizza-item"><div class="detail"><p class="name">Spicy BBQ Chicken</p><p class="desc">Chicken Breast, Hickory BBQ Sauce,<br>Red Onions &amp; Banana Peppers</p></div><div class="prices"><span>$14.49</span><span>$35.95</span></div></li>
    <li class="pizza-item"><div class="detail"><p class="name">Sweet Chili Chicken</p><p class="desc">Chicken Breast, Pineapple,<br>Red Onions &amp; Sweet Chili Sauce</p></div><div class="prices"><span>$14.49</span><span>$35.95</span></div></li>
    <li class="pizza-item"><div class="detail"><p class="name">Chicken Club</p><p class="desc">Chicken Breast, Double Smoked Bacon,<br>Red Onions and Tomatoes</p></div><div class="prices"><span>$14.79</span><span>$35.95</span></div></li>
    <li class="pizza-item"><div class="detail"><p class="name">Athenean</p><p class="desc">Chicken Breast, Spinach, Feta Cheese and Tomato</p></div><div class="prices"><span>$14.49</span><span>$34.95</span></div></li>
    <li class="pizza-item"><div class="detail"><p class="name">Greek Supreme</p><p class="desc">Chicken Breast, Feta Cheese, Tomato,<br>Green Pepper, Red Onions &amp; Black Olives</p></div><div class="prices"><span>$14.99</span><span>$35.95</span></div></li>
    <li class="pizza-item"><div class="detail"><p class="name">Mediterranean Chicken</p><p class="desc">Seasoned Chicken Breast, Tomatoes,<br>Red Onions and Feta Cheese</p></div><div class="prices"><span>$14.79</span><span>$35.95</span></div></li>
    <li class="pizza-item"><div class="detail"><p class="name">Original Spinach</p><p class="desc">Spinach &amp; Feta Cheese</p></div><div class="prices"><span>$13.49</span><span>$32.95</span></div></li>
    <li class="pizza-item"><div class="detail"><p class="name">Zeus</p><p class="desc">Spinach, Feta Cheese and Tomatoes</p></div><div class="prices"><span>$13.95</span><span>$33.95</span></div></li>
    <li class="pizza-item"><div class="detail"><p class="name">Greek</p><p class="desc">Feta Cheese, Tomato, Green Peppers,<br>Red Onions and Black Olives</p></div><div class="prices"><span>$13.99</span><span>$33.95</span></div></li>
    <li class="pizza-item"><div class="detail"><p class="name">Vegetarian</p><p class="desc">Mushrooms, Tomatoes,<br>Green Peppers and Black Olives</p></div><div class="prices"><span>$13.49</span><span>$32.95</span></div></li>
    <li class="pizza-item"><div class="detail"><p class="name">Veggie Delight</p><p class="desc">Mushrooms, Tomatoes, Green Peppers,<br>Black Olives &amp; Onions</p></div><div class="prices"><span>$13.95</span><span>$33.95</span></div></li>
    <li class="pizza-item"><div class="detail"><p class="name">Deluxe</p><p class="desc">Pepperoni, Mushrooms, Ham, Tomatoes,<br>Green Peppers and Red Onions</p></div><div class="prices"><span>$14.49</span><span>$34.95</span></div></li>
    <li class="pizza-item"><div class="detail"><p class="name">Calder Special</p><p class="desc">Pepperoni, Mushrooms, Ham,<br>Green Peppers and Black Olives</p></div><div class="prices"><span>$14.49</span><span>$34.95</span></div></li>
    <li class="pizza-item"><div class="detail"><p class="name">Dill Pickle</p><p class="desc">Crispy Dill Pickles,<br>Fresh Dill with our cream based garlic sauce.<br>Served with our without bacon.</p></div>
      <div class="prices prices--stacked"><div><span>$13.49</span><span>$32.95</span></div><div>or</div><div><span>$14.49</span><span>$35.95</span></div></div></li>
    <li class="pizza-item"><div class="detail"><p class="name">BBQ Pulled Pork</p><p class="desc">Pulled Pork, Red Onions, Red Peppers and Cilantro</p></div><div class="prices"><span>$14.49</span><span>$35.95</span></div></li>
  </ul>

  <svg class="band band--bottom" viewBox="0 0 477 86" preserveAspectRatio="none" aria-hidden="true">
    <path fill="var(--brand-red)" d="M0 6L14 3L28 6L42 2L56 5L70 3L84 6L98 2L112 5L126 3L140 6L154 2L168 5L182 3L196 6L210 2L224 5L238 3L252 6L266 2L280 5L294 3L308 6L322 2L336 5L350 3L364 6L378 2L392 5L406 3L420 6L434 2L448 5L462 3L477 5V86H0Z"/>
  </svg>
  <div class="pizza-photo pizza-photo--hero" role="img" aria-label="Photo of a whole supreme pizza with basil leaves"></div>
  <div class="brand">
    <p class="brand-name">Calder Pizza</p>
    <p class="brand-url">calderpizza.ca</p>
  </div>
</section>

</body>
</html>
```